Harwick Legal

To update and modernize current business card appearance. Marta's business is based in Melbourne with 4 other lawyers in the firm. Marta travels to the Pilbara in Western Australia approximately 1 week a month as part of the firms legal work. She consults with clients in Newman, Tom Price and Port Hedland. The lawyers work mostly from a home office, apart from court appearances. They have a virtual office in Melbourne city, and use facilities in 3 or 4 other locations around Melbourne. It is important the client's think this is a conventional law firm with a permanent office. Our business structure is a difficult concept for them to grasp. The business has been operational for 3 years, growing from 1 lawyer to 4 lawyers during that time. Our website is www.Harwicklegal.example.au and is currently being upgraded as we are not happy with its content. The logo is currently orange and dark grey but the orange is a difficult colour to reproduce and often turns out "poo" brown when documents are printed. We need clients to know we are user friendly and caring - and not head up our rears ends as some lawyers appear to be.
Updates

Thank you for the feedback so far. 1. Some of the designs have too much black (We prefer darker grey & not too much.) 2. Happy for designers to play around with different colours & logo design. What we're after is a modern look and business card that people say "wow" when they pick it up.

Industry/Entity Type

Business

```html
<!DOCTYPE html>
<html lang="en">
<head>
<meta charset="utf-8">
<title>Harwick Legal – Business Card</title>
<link rel="stylesheet" href="https://fonts.googleapis.com/css2?family=Crimson+Text:wght@400;600;700&family=PT+Sans:wght@400&display=swap">
<style>
  :root {
    --page-bg: #e3e3e4;
    --brand-red: #a50d14;
    --slate-dark: #5c5d60;
    --slate-light: #727376;
    --card-light: #efeff0;
    --ink: #111111;
    --ink-muted: #666769;
    --white: #ffffff;
    --serif: "Crimson Text", Georgia, serif;
    --sans: "PT Sans", Arial, sans-serif;
  }
  * { box-sizing: border-box; margin: 0; padding: 0; }
  html, body {
    width: 1200px; height: 1200px; overflow: hidden;
    background: var(--page-bg);
  }
  .card {
    position: absolute; left: 216px; width: 764px;
    font-family: var(--serif);
  }

  /* Front face */
  .card--front { top: 130px; height: 462px; }
  .front__banner {
    position: absolute; left: 0; top: 0; width: 100%; height: 176px;
    background: var(--brand-red);
  }
  .front__tagline {
    position: absolute; top: 16px; width: 100%; text-align: center;
    color: var(--white); font-size: 20px; letter-spacing: 0.5px; word-spacing: 12px;
  }
  .front__body {
    position: absolute; left: 0; top: 176px; width: 100%; height: 286px;
    background: radial-gradient(ellipse 60% 80% at 65% 40%, var(--slate-light), var(--slate-dark));
  }
  .front__brand {
    position: absolute; top: 180px; width: 100%; text-align: center;
    color: var(--white); font-size: 44px; font-weight: 400; letter-spacing: 2px;
    line-height: 56px;
  }
  .services {
    position: absolute; left: 52px; top: 266px; color: var(--white); list-style: none;
  }
  .services__area { font-size: 27px; font-weight: 700; line-height: 34px; }
  .services__item { font-size: 22px; line-height: 27px; }
  .services__area--second { margin-top: 8px; }
  .front__web {
    position: absolute; right: 56px; top: 418px;
    color: var(--white); font-size: 21px;
  }

  /* Back face */
  .card--back { top: 599px; height: 463px; background: var(--card-light); overflow: hidden; }
  .back__brand {
    position: absolute; left: 26px; width: 270px; top: 116px; text-align: center;
    color: var(--slate-dark); font-size: 34px; letter-spacing: 1px;
  }
  .profile { position: absolute; left: 380px; top: 22px; }
  .profile__name { font-size: 31px; font-weight: 700; color: var(--ink); line-height: 38px; }
  .profile__credentials { font-size: 21px; color: var(--ink-muted); line-height: 26px; }
  .profile__title { font-size: 28px; color: var(--ink); line-height: 38px; }

  .contacts { position: absolute; left: 350px; top: 298px; list-style: none; }
  .contacts__row {
    display: flex; align-items: center; height: 32px; white-space: nowrap;
    font-family: var(--sans); font-size: 22px; color: var(--ink);
  }
  .contacts__row--serif { font-family: var(--serif); font-size: 22px; }
  .contacts__row--web { margin-top: 10px; }
  .contacts__icon { width: 22px; height: 22px; margin-right: 10px; flex: none; }
  .back__footer { position: absolute; left: 0; bottom: 0; width: 764px; height: 34px; }
</style>
</head>
<body>

<section class="card card--front" aria-label="Card front">
  <div class="front__banner">
    <p class="front__tagline">EXPERIENCE SUPPORT SOLUTIONS</p>
  </div>
  <div class="front__body"></div>
  <p class="front__brand">Harwick Legal</p>
  <ul class="services">
    <li class="services__area">Family Law</li>
    <li class="services__item">Collaborative Practice</li>
    <li class="services__item">Mediation &amp; Negotiation</li>
    <li class="services__item">Intervention Orders</li>
    <li class="services__area services__area--second">Criminal Law</li>
  </ul>
  <p class="front__web">www.Harwicklegal.example.au</p>
</section>

<section class="card card--back" aria-label="Card back">
  <p class="back__brand">Harwick Legal</p>

  <div class="profile">
    <p class="profile__name">J. Marta Dunmore</p>
    <p class="profile__credentials">LLB(Hons) - Accredited Mediator</p>
    <p class="profile__title">Principal Solicitor</p>
  </div>

  <ul class="contacts">
    <li class="contacts__row">
      <svg class="contacts__icon" viewBox="0 0 24 24" aria-hidden="true"><path fill="#a50d14" d="M6 3c1 0 2 2 3 4s-1 3-1 4 3 4 4 4 2-2 4-1 4 2 4 3-2 4-5 4C10 21 3 14 3 8c0-3 2-5 3-5z"/></svg>
      1300 Harwick (427 942)
    </li>
    <li class="contacts__row">
      <svg class="contacts__icon" viewBox="0 0 24 24" aria-hidden="true"><rect x="7" y="3" width="10" height="18" rx="2" fill="#a50d14"/><rect x="9" y="6" width="6" height="7" fill="#efeff0"/></svg>
      0400 555 218
    </li>
    <li class="contacts__row contacts__row--serif">
      <svg class="contacts__icon" viewBox="0 0 24 24" aria-hidden="true"><rect x="3" y="6" width="18" height="12" fill="#a50d14"/><path d="M3 6l9 7 9-7" fill="none" stroke="#efeff0" stroke-width="1.5"/></svg>
      marta.dunmore@harwicklegal.example.au
    </li>
    <li class="contacts__row contacts__row--serif contacts__row--web">
      <svg class="contacts__icon" viewBox="0 0 24 24" aria-hidden="true"><g fill="none" stroke="#a50d14" stroke-width="1.8"><circle cx="12" cy="12" r="8.5"/><ellipse cx="12" cy="12" rx="3.8" ry="8.5"/><path d="M3.5 12h17M5 8h14M5 16h14"/></g></svg>
      www.Harwicklegal.example.au
    </li>
  </ul>

  <svg class="back__footer" viewBox="0 0 764 34" preserveAspectRatio="none" aria-hidden="true">
    <defs>
      <linearGradient id="footerGrey" x1="0" x2="1" y1="0" y2="0">
        <stop offset="0" stop-color="#6a6b6e"/>
        <stop offset="1" stop-color="#8a8b8e"/>
      </linearGradient>
    </defs>
    <polygon points="330,14 764,14 764,34 344,34" fill="url(#footerGrey)"/>
    <polygon points="0,0 318,0 338,34 0,34" fill="#a50d14"/>
  </svg>
</section>

</body>
</html>
```